New business card for civil engineering company - "Keystone Audit"

We need a business card designed for our new structural engineering company.

The company name is "Keystone Audit" logo files attached.

We would like the following:
* Two-sided card
* Simple design

Information to be placed on the card:
Name - Marcus Dellow
Job Title - Director / Structural Engineer
Credentials - BEng(Hons), CPEng, CMengNZ, IntPE(NZ)
Email - marcus.dellow@keystoneaudit.co.nz
mobile - 0219364058
website - www.keystoneaudit.co.nz

```html
<!DOCTYPE html>
<html lang="en">
<head>
<meta charset="utf-8">
<title>Keystone Audit — Business Card</title>
<link href="https://fonts.googleapis.com/css2?family=Playfair+Display:wght@700&family=Libre+Caslon+Text:wght@400&display=swap" rel="stylesheet">
<style>
  :root {
    --page: #efefef;
    --card-top: #2f5f89;
    --card-bottom: #154274;
    --ink: #ffffff;
    --divider: #f4f6f9;
  }
  * { margin: 0; padding: 0; box-sizing: border-box; }
  html, body {
    width: 1200px;
    height: 1096px;
    overflow: hidden;
    background: var(--page);
  }
  .canvas { position: relative; width: 1200px; height: 1096px; }
  .card {
    position: absolute;
    width: 550px;
    height: 356px;
    background: linear-gradient(180deg, var(--card-top) 0%, var(--card-bottom) 100%);
    color: var(--ink);
    overflow: hidden;
  }
  .card--back { left: 492px; top: 168px; }
  .card--front { left: 197px; top: 570px; }

  .brand-name {
    position: absolute;
    font-family: "Libre Caslon Text", serif;
    font-weight: 400;
    color: var(--ink);
    letter-spacing: 0.06em;
    white-space: nowrap;
    transform: translateX(-50%);
  }
  .card--back .brand-name { left: 50%; top: 218px; font-size: 22px; }
  .card--front .brand-name { left: 127px; top: 240px; font-size: 24px; }

  .divider {
    position: absolute;
    left: 254px;
    top: 0;
    width: 2px;
    height: 100%;
    background: var(--divider);
  }

  .details { position: absolute; left: 297px; top: 0; right: 0; bottom: 0; }
  .person-name {
    position: absolute;
    top: 44px;
    font-family: "Playfair Display", serif;
    font-weight: 700;
    font-size: 31px;
    letter-spacing: -0.01em;
    white-space: nowrap;
  }
  .person-role, .person-credentials {
    position: absolute;
    font-family: "Libre Caslon Text", serif;
    font-size: 12px;
    white-space: nowrap;
  }
  .person-role { top: 97px; }
  .person-credentials { top: 125px; }

  .contact { position: absolute; left: 0; list-style: none; }
  .contact li {
    position: absolute;
    left: 0;
    display: flex;
    align-items: center;
    height: 26px;
    white-space: nowrap;
    font-family: "Libre Caslon Text", serif;
    font-size: 11.5px;
  }
  .contact li:nth-child(1) { top: 210px; }
  .contact li:nth-child(2) { top: 245px; }
  .contact li:nth-child(3) { top: 282px; }
  .contact-icon { width: 25px; height: 25px; flex: none; margin-right: 17px; }
</style>
</head>
<body>
<main class="canvas">

  <section class="card card--back" aria-label="Card back">
    <p class="brand-name">Keystone Audit</p>
  </section>

  <section class="card card--front" aria-label="Card front">
    <p class="brand-name">Keystone Audit</p>
    <div class="divider"></div>

    <div class="details">
      <h1 class="person-name">Marcus Dellow</h1>
      <p class="person-role">Director / Structural Engineer</p>
      <p class="person-credentials">BEng(Hons), CPEng, CMengNZ, IntPE(NZ)</p>

      <ul class="contact">
        <li>
          <svg class="contact-icon" viewBox="0 0 25 25" aria-hidden="true">
            <rect x="1" y="5.5" width="23" height="14" fill="#fff"/>
            <path d="M1.5 6 L12.5 14 L23.5 6 M1.5 19 L9.5 12 M23.5 19 L15.5 12" stroke="#1f4c7d" stroke-width="1.3" fill="none"/>
          </svg>
          <span>marcus.dellow@keystoneaudit.co.nz</span>
        </li>
        <li>
          <svg class="contact-icon" viewBox="0 0 25 25" aria-hidden="true">
            <path d="M6 2 L9.5 6.5 L7.3 9.2 C8.7 12.3 11.6 15.4 15 17 L17.6 14.8 L22.5 18.5 L20 22.5 C11 22 3 13.8 2.5 5 Z" fill="#fff"/>
          </svg>
          <span>0219364058</span>
        </li>
        <li>
          <svg class="contact-icon" viewBox="0 0 25 25" aria-hidden="true" fill="none" stroke="#fff" stroke-width="1.6">
            <circle cx="12.5" cy="12.5" r="11"/>
            <ellipse cx="12.5" cy="12.5" rx="5" ry="11"/>
            <path d="M1.5 12.5 H23.5 M3.5 6.5 H21.5 M3.5 18.5 H21.5 M12.5 1.5 V23.5"/>
          </svg>
          <span>www.keystoneaudit.co.nz</span>
        </li>
      </ul>
    </div>
  </section>

</main>
</body>
</html>
```